Educational non-profit needs an End of the Year Flyer

We need a flyer to mail to our supporters asking for donations to our program. Hillcrest Open Learning Hub runs after school programs for low-income students in Pasadena, CA. This is our end of the year mailing to supporters asking them to finish out the year with their contributions so that we can meet our budget.

Target Market(s)

Donors and supporters of organization

Industry/Entity Type

Non-Profit

Font styles to use
Serif

Colors

Designer to choose colors to be used in the design.

Requirements
Must have
• The project should fit on a 6x9" card, and be printed on front and back. It should show pictures, use the copy I have included, a space for a label address, a stamp, and the return address.
Nice to have
• eye-catching, fun

```html
<!DOCTYPE html>
<html lang="en">
<head>
<meta charset="utf-8">
<title>Hillcrest Open Learning Hub – Year End Postcard</title>
<link href="https://fonts.googleapis.com/css2?family=Raleway:wght@400;500;600;700&family=Playball&display=swap" rel="stylesheet">
<style>
:root{
  --yellow:#fecb00;
  --ink:#1d1d1d;
  --white:#ffffff;
  --slate:#4b4b4d;
  --mist:#d6d6d8;
  --backdrop:#a3a3a3;
  --photo-dark:#2f2a26;
}
*{box-sizing:border-box;margin:0;padding:0}
html,body{width:960px;height:1200px;overflow:hidden}
body{background:var(--backdrop);font-family:"Raleway",sans-serif;color:var(--ink);position:relative}
.card{position:absolute;left:114px;width:734px;height:490px;background:var(--white);overflow:hidden}
.card--front{top:67px}
.card--back{top:638px}
.abs{position:absolute}

/* front */
.brand-mark{left:30px;top:28px;width:52px;height:52px;border-radius:50%;background:var(--yellow)}
.brand-name{left:117px;top:42px;font-size:20px;font-weight:500;line-height:24px;letter-spacing:.3px;color:var(--ink)}
.hero-band{left:0;top:110px;width:734px;height:236px}
.headline{left:30px;top:148px;font-size:27px;font-weight:700;line-height:32px;color:var(--yellow)}
.hero-copy{left:30px;top:262px;width:380px;font-size:13px;line-height:16px;color:var(--white);font-weight:500}
.child-photo{left:520px;top:0;width:170px;height:468px;border-radius:60px 60px 20px 20px;background:linear-gradient(180deg,#3a3336 0%,#1f2a44 45%,#cfc7b8 75%,#d9a1b8 100%)}
.greeting{left:28px;top:350px;font-family:"Playball",cursive;font-size:42px;color:var(--yellow)}
.greeting-sub{left:30px;top:410px;font-size:18px;font-weight:600}
.front-footer{left:0;top:442px;width:734px;height:48px;background:var(--yellow)}
.contact-row{left:30px;top:456px;display:flex;align-items:center;gap:16px;font-size:12px;font-weight:500}
.contact-row span{display:flex;align-items:center;gap:8px}
.corner-stripe{left:650px;top:442px}

/* back */
.appeal-panel{left:0;top:0;width:367px;height:342px;background:var(--slate)}
.story-box{left:10px;top:10px;width:347px;height:182px;background:var(--mist)}
.story-title{left:20px;top:21px;width:330px;font-size:16px;font-weight:700;line-height:19px;white-space:nowrap}
.gallery-photo{top:75px;height:107px;border:2px solid var(--yellow)}
.budget-box{left:10px;top:200px;width:347px;height:40px;background:var(--ink);color:var(--yellow);font-size:13.5px;line-height:16px;text-align:center;padding-top:4px;font-weight:500}
.ask{left:0;width:367px;text-align:center;font-size:12.5px;font-weight:600;color:var(--yellow)}
.link-box{left:55px;top:290px;width:255px;height:44px;background:var(--ink);text-align:center;color:var(--white);font-size:13px;padding-top:3px}
.link-box b{display:block;margin:3px auto 0;width:200px;background:var(--yellow);color:var(--ink);font-size:16px;font-weight:500;line-height:18px}
.return-panel{left:0;top:342px;width:367px;height:148px;background:var(--yellow)}
.return-name{left:18px;top:364px;font-size:12px;font-weight:700}
.return-list{left:18px;top:380px;list-style:none;font-size:12px;font-weight:500}
.return-list li{display:flex;align-items:center;gap:6px;height:20.5px}
.mail-mark{left:400px;top:24px;width:50px;height:50px;border-radius:50%;background:var(--yellow)}
.mail-address{left:461px;top:48px;font-size:9px;line-height:11px}
.stamp-box{left:624px;top:29px;width:82px;height:82px;border:1px solid #555}
.address-line{left:502px;width:204px;height:1px;background:#555}
</style>
</head>
<body>

<section class="card card--front">
  <div class="abs brand-mark"></div>
  <div class="abs brand-name">HILLCREST OPEN<br>LEARNING HUB</div>

  <svg class="abs hero-band" viewBox="0 0 734 236" width="734" height="236">
    <rect width="734" height="236" fill="#fecb00"/>
    <polygon points="0,0 478,0 416,236 0,236" fill="#2f2a26" role="img" aria-label="Dimmed photo of children sitting together on playground swings"/>
  </svg>
  <div class="abs headline">We need your help to<br>finish out 2018 strong!</div>
  <p class="abs hero-copy">We have had a wonderful 25th year of serving the children and families of Pasadena here at Hillcrest Open Learning Hub with high quality afterschool programs.</p>

  <div class="abs child-photo" role="img" aria-label="Cut-out photo of a smiling young girl hanging from a playground ring"></div>

  <div class="abs greeting">Merry Christmas</div>
  <div class="abs greeting-sub">from all of us at HOLH!</div>

  <div class="abs front-footer"></div>
  <div class="abs contact-row">
    <span><svg width="24" height="24" viewBox="0 0 24 24" fill="none" stroke="#1d1d1d" stroke-width="1.4"><circle cx="12" cy="12" r="10.5"/><ellipse cx="12" cy="12" rx="4.5" ry="10.5"/><path d="M1.5 12h21M3.5 6.5h17M3.5 17.5h17"/></svg>www.brightpathkids.org</span>
    <span><svg width="24" height="20" viewBox="0 0 24 20" fill="none" stroke="#1d1d1d" stroke-width="1.5"><rect x="1" y="2" width="22" height="16"/><path d="M1 2l11 9 11-9M1 18l8-7M23 18l-8-7"/></svg>info@brightpathkids.org</span>
    <span><svg width="24" height="24" viewBox="0 0 24 24" fill="none" stroke="#1d1d1d" stroke-width="1.4"><circle cx="12" cy="12" r="10.5"/></svg>Hillcrest Open Learning Hub</span>
  </div>
  <svg class="abs corner-stripe" width="84" height="48" viewBox="0 0 84 48">
    <polygon points="0,0 60,0 84,48 24,48" fill="#ffffff"/>
    <polygon points="30,0 36,0 60,48 54,48" fill="#1d1d1d"/>
  </svg>
</section>

<section class="card card--back">
  <div class="abs appeal-panel"></div>
  <div class="abs story-box"></div>
  <div class="abs story-title">Hundreds and hundreds of students have<br>been a part of the Bright Kids Club family.</div>
  <div class="abs gallery-photo" style="left:21px;width:73px;background:linear-gradient(160deg,#2a1c22,#c2577f)" role="img" aria-label="Photo of two girls hugging"></div>
  <div class="abs gallery-photo" style="left:102px;width:164px;background:linear-gradient(180deg,#c8b79c,#3a2e2c)" role="img" aria-label="Photo of a group of girls holding basketballs in a gym"></div>
  <div class="abs gallery-photo" style="left:273px;width:76px;background:linear-gradient(170deg,#d8d2c6,#b7323c)" role="img" aria-label="Photo of children serving food at a table"></div>

  <div class="abs budget-box">Our annual budget is $275,000 and we count on<br>$100,000 from individual donors.</div>
  <div class="abs ask" style="top:254px">Will you join with us for an end of the year contribution?</div>
  <div class="abs ask" style="top:274px">Remember, you can give online through GiveEasy.</div>
  <div class="abs link-box">Just look for the link on our website -<b>www.brightpathkids.org.</b></div>

  <div class="abs return-panel"></div>
  <div class="abs return-name">Hillcrest Open Learning Hub</div>
  <ul class="abs return-list">
    <li><svg width="12" height="12" viewBox="0 0 12 12" fill="none" stroke="#1d1d1d"><path d="M6 11s4-4 4-6.5a4 4 0 0 0-8 0C2 7 6 11 6 11z"/><circle cx="6" cy="4.5" r="1.3"/></svg>418 N. Larchmont Ave. Pasadena, CA 91104</li>
    <li><svg width="12" height="12" viewBox="0 0 12 12" fill="none" stroke="#1d1d1d"><circle cx="6" cy="6" r="5.3"/><path d="M4 3.5l1 1.5-.7.8a4 4 0 0 0 1.9 1.9l.8-.7 1.5 1-.8 1C5.5 8.5 3.5 6.5 3 4.3z"/></svg>(626) 555-0147</li>
    <li><svg width="12" height="10" viewBox="0 0 12 10" fill="none" stroke="#1d1d1d"><rect x=".5" y=".5" width="11" height="9"/><path d="M.5 .5L6 5l5.5-4.5"/></svg>info@brightpathkids.org</li>
    <li><svg width="12" height="12" viewBox="0 0 12 12" fill="none" stroke="#1d1d1d"><circle cx="6" cy="6" r="5.3"/><ellipse cx="6" cy="6" rx="2.3" ry="5.3"/><path d="M.7 6h10.6"/></svg>www.brightpathkids.org</li>
    <li><svg width="12" height="12" viewBox="0 0 12 12" fill="none" stroke="#1d1d1d"><circle cx="6" cy="6" r="5.3"/></svg>Hillcrest Open Learning Hub</li>
  </ul>

  <div class="abs mail-mark"></div>
  <div class="abs mail-address">Hillcrest Open Learning Hub<br>418 N. Larchmont Ave.<br>Pasadena, CA 91104</div>
  <div class="abs stamp-box"></div>
  <div class="abs address-line" style="top:223px"></div>
  <div class="abs address-line" style="top:254px"></div>
  <div class="abs address-line" style="top:286px"></div>
  <div class="abs address-line" style="top:317px"></div>
</section>

</body>
</html>
```